Diesel Fitting/Mechanical Company Needs a new Business Card

We would like a new business card that showcases our logo and business information.

Industry/Entity Type

Business

Contact Information for Business Card

314 Wendale Street
PO Box 7581 KELLAVALE QLD 4796
Phone: 49312787 Fax: 49312688 Mobile: 0438915276 ABN: 63 519 087 342

Requirements
Must have
• The following email addresses:
• admin@tkservicing.com.au , sales@tkservicing.com.au , accounts@tkservicing.com.au , parts@tkservicing.com.au , office@tkservicing.com.au
• Also need to have the website: www.tkservicing.com.au

```html
<!DOCTYPE html>
<html lang="en">
<head>
<meta charset="utf-8">
<title>TK Servicing – Business Card</title>
<link rel="stylesheet" href="https://fonts.googleapis.com/css2?family=Open+Sans:wght@400;600&display=swap">
<style>
  :root {
    --backdrop: #5a3d2b;
    --card-light: #ffffff;
    --card-dark: #232323;
    --ink: #3b3b3b;
    --orange: #f47a20;
    --yellow: #fbbf1a;
    --red: #e3242b;
  }
  * { margin: 0; padding: 0; box-sizing: border-box; }
  html, body { width: 1200px; height: 1000px; overflow: hidden; }
  body {
    background: var(--backdrop);
    font-family: "Open Sans", Arial, sans-serif;
    position: relative;
  }
  .card {
    position: absolute;
    left: 265px;
    width: 667px;
    box-shadow: 0 6px 16px rgba(0,0,0,.45);
  }
  .card--front { top: 75px; height: 396px; background: var(--card-light); }
  .card--back { top: 533px; height: 397px; background: var(--card-dark); }

  .contact { position: absolute; left: 33px; top: 26px; color: var(--ink); }
  .contact__name { color: var(--orange); font-size: 22px; font-weight: 600; line-height: 1.2; letter-spacing: .2px; }
  .contact__role { font-size: 16px; margin-bottom: 8px; }
  .contact__line { font-size: 16px; line-height: 22.5px; display: flex; align-items: center; gap: 5px; }
  .contact__line svg { width: 14px; height: 14px; fill: var(--orange); flex: none; }
  .contact__label { color: var(--orange); }
  .contact__emails { font-size: 16px; line-height: 22.3px; }
  .contact__abn { font-size: 16px; line-height: 22px; margin-top: 4px; }
  .contact__abn b { color: var(--orange); font-weight: 600; }
  .contact__address { font-size: 16px; line-height: 21px; margin-top: 4px; }

  .brand {
    position: absolute;
    display: flex; align-items: center; gap: 14px;
    font-weight: 600; color: var(--orange);
  }
  .card--front .brand { left: 345px; top: 180px; font-size: 38px; }
  .card--back .brand { left: 0; right: 0; top: 165px; justify-content: center; font-size: 46px; }
  .brand__dot { width: 26px; height: 26px; border-radius: 50%; background: var(--yellow); flex: none; }
  .card--back .brand__dot { width: 32px; height: 32px; }

  .band { position: absolute; left: 0; bottom: 0; width: 667px; height: 28px; }
  .band__web {
    position: absolute; left: 33px; bottom: 4px;
    color: #fff; font-size: 16px; letter-spacing: 1px;
  }
</style>
</head>
<body>

<section class="card card--front">
  <div class="contact">
    <div class="contact__name">DARREN KOSTEL</div>
    <div class="contact__role">Managing Director</div>
    <div class="contact__line">
      <svg viewBox="0 0 16 16"><path d="M1 5c0-2 2-3 7-3s7 1 7 3v1h-4V4.5H5V6H1zM3 7h10l2 6H1z"/></svg>49312787
    </div>
    <div class="contact__line">
      <svg viewBox="0 0 16 16"><path d="M4 0h8v16H4zM5.5 2v10h5V2z"/></svg>0438915276
    </div>
    <div class="contact__line">
      <svg viewBox="0 0 16 16"><path d="M4 1h8v4H4zM1 6h14v6h-3v3H4v-3H1zM5 10v4h6v-4z"/></svg>49312688
    </div>
    <div class="contact__line contact__label" style="margin-top:2px">
      <svg viewBox="0 0 16 16"><path d="M1 3h14v1L8 9 1 4zM1 6l7 5 7-5v7H1z"/></svg>Email
    </div>
    <div class="contact__emails">
      admin@tkservicing.com.au<br>
      sales@tkservicing.com.au<br>
      accounts@tkservicing.com.au<br>
      parts@tkservicing.com.au<br>
      office@tkservicing.com.au
    </div>
    <div class="contact__abn"><b>ABN:</b> 63 519 087 342</div>
    <div class="contact__address">
      314 Wendale Street<br>
      PO Box 7581 KELLAVALE QLD 4796
    </div>
  </div>

  <div class="brand"><span class="brand__dot"></span>TK Servicing</div>

  <svg class="band" viewBox="0 0 667 28" aria-hidden="true">
    <polygon points="0,0 383,0 400,28 0,28" fill="var(--orange)"/>
    <polygon points="391,0 535,0 552,28 408,28" fill="var(--yellow)"/>
    <polygon points="543,0 667,0 667,28 560,28" fill="var(--red)"/>
  </svg>
  <div class="band__web">www.tkservicing.com.au</div>
</section>

<section class="card card--back">
  <div class="brand"><span class="brand__dot"></span>TK Servicing</div>
</section>

</body>
</html>
```